Clean book cover design for book about writing a book

Book title: The Crossing
Subtitle: 9 Paths to Crafting a Volume that Counts
Name: Marisol T. Brenwick, The Quill Nursery

This is a book which teaches 10 steps to writing a self-help book. I'm looking for a very clean impactful cover either with no image or just a small simple image of a book, typewriter, laptop, cabin or something very simple. I am attaching the manuscript here if reading it would help you with the cover. The theme of the book is that you can write with joy and ease and your book can just flow out of you if you learn how to clear the blocks between you and your book already written. Sort of a new agey stance on book writing.

The book should generally match the branding on my website. Www.TheQuillNursery.example.

I have photos of myself attached which I'd like used for the back cover with an "about the author section of maybe 50 words.

The project is for the full back cover and spine as well as the front cover (see print Forge template attached) but to win the contest you can just design the front cover and then I'll give the winner the template for the full design with the back cover copy. Or you can design the full cover using the template and you can use Loren ipsum text if you need to.

My clients are very upmarket and the themes of my business revolve around nuturing and incubating ideas and authors. Very feminine creation energy.

For colors see The Crossing Press (CB) wax seals and the background fades. I don't want my logo on the cover but I am attaching it here so you get a feel for the branding. The logo is in the LOBSTER font and you can see how we do the grey with the rainbow shadow.

Here are some covers I like:

http://www.shopvale.example/Pen-Tome-Quick-Stage---Stage/dp/055817342Q
http://www.shopvale.example/Plotting-Your-Tale-Chart-Triumph/dp/0841739265
http://www.shopvale.example/Be-Scribe-Seeking-Voice-Guide-ebook/dp/K22R9WQ3L1
http://www.shopvale.example/Strays-Tale-Triumph-Rupert-Vanhollow/dp/0552048871
Updates

I have revised my brief to include some picture and images that will help you create the cover. I have also included some of my favorite covers to give you more of a sense of what I'm going for. And I have included the manuscript in case it would help you to skim through it in order to get a sense of the reader and the book. I think if you look at my revised brief it will make it easier to create a submission. Thanks!

Target Market(s)

Women 40-60 who run small businesses as life coaches or other healing jobs (therapy, reiki, light work) they have a spiritual/new age bent.

Industry/Entity Type

Business

Font styles to use
Serif
Other font styles liked:
• Lobster (not required... just a suggestion since it's my logo font)

Requirements
Must have
• Name and title easy to read in 1" x 1" thumb nail
Nice to have
• Fantastic type face treatment.

Match the look and feel of my website.
Should not have
• Busy images. With one simple image or just designed with colors and typeface treatment

```html
<!DOCTYPE html>
<html lang="en">
<head>
<meta charset="utf-8">
<title>The Crossing — Front Cover</title>
<link rel="stylesheet" href="https://fonts.googleapis.com/css2?family=Architects+Daughter&family=Roboto:wght@500&family=Varela+Round&display=swap">
<style>
  :root {
    --stage-grey: #b6b6b6;
    --sky-blue: #5e9fea;
    --lilac: #b9b2f2;
    --blush-pink: #f2b6ec;
    --orchid: #e488e0;
    --title-red: #d10a0a;
    --title-red-dark: #a80000;
    --title-outline: #ffffff;
    --title-shadow: rgba(60, 40, 70, 0.75);
    --ink-dark: #3a3a3a;
    --ink-mid: #4a4a4a;
    --book-red: #c20a0a;
    --book-red-light: #e04040;
  }

  html, body {
    margin: 0;
    padding: 0;
    width: 1200px;
    height: 1200px;
    overflow: hidden;
    background: var(--stage-grey);
  }

  .canvas {
    position: relative;
    width: 1200px;
    height: 1200px;
  }

  .cover {
    position: absolute;
    left: 260px;
    top: 90px;
    width: 680px;
    height: 1020px;
    overflow: hidden;
    background:
      radial-gradient(ellipse at 30% 30%, rgba(255,255,255,0.18), rgba(255,255,255,0) 60%),
      linear-gradient(90deg, var(--sky-blue) 0%, #78a8f0 28%, var(--lilac) 50%, var(--blush-pink) 72%, var(--orchid) 100%);
    box-shadow: 0 12px 30px rgba(0,0,0,0.25);
  }

  .cover__title {
    position: absolute;
    left: 0;
    right: 0;
    top: 110px;
    margin: 0;
    text-align: center;
    font-family: "Roboto", Arial, sans-serif;
    font-weight: 500;
    font-size: 136px;
    line-height: 132px;
    letter-spacing: -1px;
    color: var(--title-red);
    -webkit-text-stroke: 3px var(--title-outline);
    paint-order: stroke fill;
    text-shadow: 3px 4px 0 var(--title-shadow);
  }

  .cover__title-line {
    display: block;
  }

  .cover__subtitle {
    position: absolute;
    left: 22px;
    right: 22px;
    top: 410px;
    height: 50px;
    margin: 0;
    display: flex;
    align-items: center;
    justify-content: center;
    border-radius: 12px;
    background: linear-gradient(180deg, var(--title-red) 0%, var(--title-red-dark) 100%);
    box-shadow: 0 0 0 2px rgba(255,255,255,0.35), 1px 2px 3px rgba(60,0,0,0.4);
    font-family: "Varela Round", Arial, sans-serif;
    font-size: 27px;
    font-weight: 400;
    color: #ffffff;
    white-space: nowrap;
  }

  .cover__emblem {
    position: absolute;
    left: 245px;
    top: 530px;
    width: 190px;
    height: 170px;
  }

  .cover__author {
    position: absolute;
    left: 0;
    right: 0;
    top: 880px;
    margin: 0;
    text-align: center;
    font-family: "Architects Daughter", cursive;
    font-size: 40px;
    font-weight: 400;
    letter-spacing: 1px;
    color: var(--ink-dark);
  }

  .cover__imprint {
    position: absolute;
    left: 0;
    right: 0;
    top: 948px;
    margin: 0;
    text-align: center;
    font-family: "Varela Round", Arial, sans-serif;
    font-size: 21px;
    color: var(--ink-mid);
  }
</style>
</head>
<body>
  <main class="canvas">
    <article class="cover">
      <h1 class="cover__title">
        <span class="cover__title-line">The</span>
        <span class="cover__title-line">Crossing</span>
      </h1>

      <p class="cover__subtitle">9 Paths to Crafting a Volume that Counts</p>

      <svg class="cover__emblem" role="img" aria-label="Illustration of a small stack of three red hardcover books" viewBox="0 0 190 170">
        <defs>
          <linearGradient id="stack-tone" x1="0" y1="0" x2="1" y2="1">
            <stop offset="0" stop-color="var(--book-red-light)"/>
            <stop offset="1" stop-color="var(--book-red)"/>
          </linearGradient>
        </defs>
        <rect x="0" y="0" width="190" height="170" rx="10" fill="url(#stack-tone)"/>
      </svg>

      <p class="cover__author">Marisol T. Brenwick</p>
      <p class="cover__imprint">The Quill Nursery</p>
    </article>
  </main>
</body>
</html>
```